Vel Norra A4 paper and card metallic new packaging

Vel Norra New Packaging Brief
We need a CLASSIC packaging design which wraps around the bottom left side of the product (A4 card) in the shape of a square (front & back) for an existing brand name call Vel Norra. This is then covered in a polybag. This needs to display the most important detail about the product on the FRONT and then the other information on the back.
See images attached of some ideas
The packaging needs to be CLEAN and simple to portray the fact the product is of a Premium Luxurious quality.
It is sold in a store where it sits on a shelf so we need the following information portrayed very clearly so the consumer can see it straight away and know what the product is:
The below points need to be shown on the FRONT of the packaging - Information is listed in order of importance.
1.Premium Luxurious Card
2. Metallic
3. A4
4.The Colour (eg, Silver)
5.25 Pack
6. Logo – this can be small

These need to be shown on the BACK of the packaging - Information is listed in order of importance.
1.PREMIUM Luxurious Card
2.
• Ideal for card making for all occasions
• Invitations for all Celebrations
• Creative card & paper for presentations
3. Acid free
4. Made in china
5. Logo – this can be small
6.Barcode

Background
Vel Norra is a brand which sells PREMIUM Luxurious Paper and card stock which can be used for card making, invites, presentations. The colour range is approx. 24 colours and it comes in metallic and weave. It includes the following
*A4 Card 260gsm & paper 120gsm
*DL & C6 envelopes 120gsm

PLEASE READ ALL UPLOADED FILE NAMES.

Target Market(s)

Office supply and invitation market

Industry/Entity Type

Store

Requirements
Must have
• Most important is to have a style of packaging that suits and displays the product. Needs to be fresh and clean packaging but also show quality and show the actual product.
• Font should be simple, easy to read, clear so consumers can read what the product is straight away.
• Colours – can match the logo but we are open to other ideas as well.
• The colour range of the card we sell is 24 different colours so the actual packaging needs to match all colours and stand out.

```html
<!DOCTYPE html>
<html lang="en">
<head>
<meta charset="utf-8">
<title>Vel Norra – Premium Luxurious Card A4 Pink</title>
<link href="https://fonts.googleapis.com/css2?family=Poiret+One&display=swap" rel="stylesheet">
<style>
  :root {
    --page: #ffffff;
    --card-top: #fafafa;
    --card-bottom: #f2f2f2;
    --wrap: #000000;
    --ink: #ffffff;
    --accent: #ec1169;
    --brand: #8a8a8a;
  }
  html, body {
    margin: 0;
    padding: 0;
    width: 1200px;
    height: 1000px;
    overflow: hidden;
    background: var(--page);
    font-family: "Poiret One", sans-serif;
  }
  .card-sheet {
    position: absolute;
    left: 418px;
    top: 0;
    width: 782px;
    height: 676px;
    background: linear-gradient(180deg, var(--card-top), var(--card-bottom));
  }
  .wrap-label {
    position: absolute;
    left: 418px;
    top: 318px;
    width: 358px;
    height: 358px;
    overflow: hidden;
    background: var(--wrap);
    color: var(--ink);
    -webkit-text-stroke: 0.7px currentColor;
  }
  .colour-swatch {
    position: absolute;
    left: 6px;
    top: 6px;
    width: 59px;
    height: 43px;
    background: var(--accent);
  }
  .brand-mark {
    position: absolute;
    left: 0;
    right: 0;
    top: 62px;
    display: flex;
    align-items: center;
    justify-content: center;
    gap: 10px;
    color: var(--brand);
    font-size: 30px;
    font-weight: 400;
  }
  .brand-mark .dot {
    width: 14px;
    height: 14px;
    border-radius: 50%;
    background: var(--brand);
  }
  .product-title {
    position: absolute;
    left: 0;
    right: 0;
    top: 144px;
    margin: 0;
    text-align: center;
    font-size: 35px;
    font-weight: 400;
    letter-spacing: 0;
    white-space: nowrap;
  }
  .size {
    position: absolute;
    left: 32px;
    width: 120px;
    top: 211px;
    text-align: center;
    font-size: 76px;
    letter-spacing: -4px;
    line-height: 1;
  }
  .pack-count {
    position: absolute;
    left: 42px;
    width: 100px;
    top: 307px;
    text-align: center;
    font-size: 25px;
    white-space: nowrap;
  }
  .finish {
    position: absolute;
    left: 178px;
    width: 100px;
    top: 214px;
    text-align: center;
    font-size: 40px;
  }
  .colour-name {
    position: absolute;
    left: 178px;
    width: 100px;
    top: 286px;
    text-align: center;
    font-size: 49px;
    color: var(--accent);
  }
</style>
</head>
<body>
  <div class="card-sheet"></div>
  <section class="wrap-label">
    <div class="colour-swatch"></div>
    <div class="brand-mark"><span class="dot"></span><span>Vel Norra</span></div>
    <h1 class="product-title">Premium Luxurious Card</h1>
    <div class="size">A4</div>
    <div class="pack-count">25 Pack</div>
    <div class="finish">Matt</div>
    <div class="colour-name">Pink</div>
  </section>
</body>
</html>
```